Velmont Realty Business Cards template for all our agents.

Create a template for Business Cards for our agents. We would need to have access to the source file in order to change info for each agent. We want color and not all white cards. We would like to see movements and texture in the design. Use the colors in the file included plus neutral colors back, white and grey. we would like to see some designs with the logo on the front and some on the back.

Target Market(s)

Real Estate

Industry/Entity Type

Real Estate

Contact Information for Business Card

Please create a template for our business cards. Dimensions 3.5 x 2

We would like
• Spot for an agent photo. (On front of card)
• Logo
• Position (mainly Domivar ®)
• Mobile
• Fax.
• Email
• Website
• Equal housing logo
• Domivar logo
• Text – “Search property listings like an agent!”
• Our address 4127 Wexmoor Lane, Suite 3, Clarksburg, MD 20594
• Our colors are attached.
• Not boxy
• DO NOT HAVE AGENT PHOTO CUT OUT.

Requirements
Must have
• • Spot for an agent photo. (On front of card)
• • Logo
• • Position (mainly Domivar ®)
• • Mobile
• • Fax.
• • Email
• • Website
• • Equal housing logo
• • Domivar logo
• • Text – “Search property listings like an agent!”
• • Our address 4127 Wexmoor Lane, Suite 3, Clarksburg, MD 20594
Should not have
• BOXY

```html
<!DOCTYPE html>
<html lang="en">
<head>
<meta charset="UTF-8">
<title>Velmont Realty Group – Agent Business Cards</title>
<link rel="stylesheet" href="https://fonts.googleapis.com/css2?family=Lato:wght@400;700;900&display=swap">
<style>
  :root {
    --stage: #3a3a3c;
    --card-white: #f7f7f5;
    --brand-green: #5e7a33;
    --brand-green-dark: #2f4a1c;
    --brand-plum: #5a2740;
    --plum-dark: #45182f;
    --pill-grey: #c9cccf;
    --text-dark: #2f3a22;
    --photo-tone-a: #c7d0d6;
    --photo-tone-b: #7a5a4a;
  }
  * { box-sizing: border-box; margin: 0; padding: 0; }
  html, body { width: 1200px; height: 997px; overflow: hidden; }
  body {
    background: var(--stage);
    font-family: "Lato", sans-serif;
    position: relative;
  }
  .card {
    position: absolute;
    left: 320px;
    width: 560px;
    height: 320px;
    border-radius: 20px;
    overflow: hidden;
    display: flex;
    box-shadow: 0 14px 30px rgba(0,0,0,.45);
  }
  .card--back { top: 130px; }
  .card--front { top: 530px; }

  /* Back side */
  .back__panel-white {
    width: 44%;
    background: var(--card-white);
    display: flex;
    flex-direction: column;
    align-items: center;
    padding: 34px 18px 24px;
  }
  .brand-mark {
    display: flex;
    align-items: center;
    gap: 8px;
  }
  .brand-mark__square {
    width: 22px; height: 22px;
    background: var(--brand-plum);
  }
  .brand-mark__name {
    font-weight: 900;
    color: var(--brand-plum);
    font-size: 20px;
    letter-spacing: .5px;
  }
  .back__brand { flex-direction: column; gap: 10px; }
  .back__brand .brand-mark__square { width: 70px; height: 70px; }
  .tagline {
    margin-top: 22px;
    text-align: center;
    font-weight: 900;
    font-size: 13px;
    line-height: 1.25;
    color: var(--brand-green-dark);
    text-transform: uppercase;
  }
  .badges {
    margin-top: auto;
    display: flex;
    gap: 26px;
    align-items: flex-end;
  }
  .badge { width: 40px; height: 40px; }

  .back__panel-green {
    flex: 1;
    background: var(--brand-green);
    color: #f1f1ea;
    display: flex;
    flex-direction: column;
    justify-content: center;
    align-items: center;
  }
  .back__name {
    font-weight: 700;
    font-size: 46px;
    letter-spacing: 2px;
    line-height: 1;
  }
  .back__sub {
    font-weight: 700;
    font-size: 22px;
    letter-spacing: 3px;
    margin-top: 6px;
  }
  .back__web {
    display: flex;
    align-items: center;
    gap: 10px;
    margin-top: 10px;
    font-size: 13px;
  }
  .back__web::before, .back__web::after {
    content: "";
    width: 60px;
    height: 1px;
    background: #f1f1ea;
  }

  /* Front side */
  .front__panel-white {
    width: 56%;
    background: var(--card-white);
    padding: 30px 22px 22px 28px;
    color: var(--text-dark);
  }
  .front__brand .brand-mark__name { font-size: 21px; }
  .front__brand .brand-mark__square { width: 38px; height: 38px; }
  .address {
    margin-top: 40px;
    font-weight: 700;
    font-size: 14px;
    line-height: 1.35;
  }
  .contact-list {
    list-style: none;
    margin-top: 14px;
    font-size: 14px;
  }
  .contact-list li {
    display: flex;
    align-items: center;
    gap: 10px;
    margin-bottom: 6px;
  }
  .contact-icon { width: 16px; height: 16px; flex: none; }
  .website {
    margin-top: 4px;
    padding-left: 26px;
    font-weight: 900;
    font-size: 17px;
  }

  .front__panel-plum {
    flex: 1;
    background: var(--brand-plum);
    position: relative;
  }
  .agent-photo {
    position: absolute;
    left: 22px;
    top: 24px;
    width: 200px;
    height: 200px;
    border-radius: 50%;
    border: 4px solid #f3f3f0;
    outline: 3px solid var(--brand-green-dark);
    outline-offset: -10px;
    background: radial-gradient(circle at 50% 45%, var(--photo-tone-b) 0 32%, var(--photo-tone-a) 60%);
  }
  .agent-pill {
    position: absolute;
    left: 10px;
    right: -20px;
    bottom: 34px;
    height: 52px;
    border-radius: 26px 0 0 26px;
    background: var(--pill-grey);
    text-align: center;
    padding-top: 8px;
    padding-right: 20px;
  }
  .agent-pill__name {
    font-weight: 900;
    font-size: 16px;
    color: var(--brand-green-dark);
    letter-spacing: .5px;
  }
  .agent-pill__title {
    font-size: 12px;
    color: #222;
  }
</style>
</head>
<body>

<section class="card card--back" aria-label="Business card, back">
  <div class="back__panel-white">
    <div class="brand-mark back__brand">
      <span class="brand-mark__square"></span>
      <span class="brand-mark__name">VELMONT REALTY</span>
    </div>
    <p class="tagline">Search property<br>listings like an agent</p>
    <div class="badges">
      <svg class="badge" viewBox="0 0 40 40" role="img" aria-label="Equal housing badge">
        <rect x="4" y="4" width="32" height="32" fill="#2b2b2b"/>
      </svg>
      <svg class="badge" viewBox="0 0 40 40" role="img" aria-label="Domivar badge">
        <rect x="6" y="6" width="28" height="28" fill="none" stroke="#2b2b2b" stroke-width="3"/>
      </svg>
    </div>
  </div>
  <div class="back__panel-green">
    <div class="back__name">VELMONT</div>
    <div class="back__sub">REALTY GROUP</div>
    <div class="back__web">www.vrg.com</div>
  </div>
</section>

<section class="card card--front" aria-label="Business card, front">
  <div class="front__panel-white">
    <div class="brand-mark front__brand">
      <span class="brand-mark__square"></span>
      <span class="brand-mark__name">VELMONT REALTY GROUP</span>
    </div>
    <p class="address">4127 Wexmoor Lane, Suite 3<br>Clarksburg, MD 20594</p>
    <ul class="contact-list">
      <li>
        <svg class="contact-icon" viewBox="0 0 16 16"><circle cx="8" cy="8" r="8" fill="#2f4a1c"/><path d="M5 4.5l1.6-.5 1 2-1 .8a5 5 0 0 0 2.6 2.6l.8-1 2 1-.5 1.6C8 11 5 8 5 4.5z" fill="#fff"/></svg>
        <span>0161 482 5907</span>
      </li>
      <li>
        <svg class="contact-icon" viewBox="0 0 16 16"><circle cx="8" cy="8" r="8" fill="#2f4a1c"/><rect x="5.5" y="3.5" width="5" height="9" rx="1" fill="#fff"/><rect x="6.3" y="4.6" width="3.4" height="5.6" fill="#2f4a1c"/></svg>
        <span>07593 618 240</span>
      </li>
      <li>
        <svg class="contact-icon" viewBox="0 0 16 16"><circle cx="8" cy="8" r="8" fill="#2f4a1c"/><rect x="4" y="5" width="8" height="6" fill="#fff"/><path d="M4 5l4 3.2L12 5" fill="none" stroke="#2f4a1c" stroke-width="1"/></svg>
        <span>mthorne@vrg.com</span>
      </li>
    </ul>
    <p class="website">www.vrg.com</p>
  </div>
  <div class="front__panel-plum">
    <div class="agent-photo" role="img" aria-label="Agent portrait photo"></div>
    <div class="agent-pill">
      <div class="agent-pill__name">MARISSA THORNE</div>
      <div class="agent-pill__title">® DOMIVAR</div>
    </div>
  </div>
</section>

</body>
</html>
```